House Builder and Property Development Card Design and Logo

I need a business card design for a building and property development company.
Colour scheme of Dark Grey and Green, I would like it bold, sharp and professional.
No logo yet done, I'm open to options but please stay away from the usual- house, roof, hammers etc.
Thanks Rob

Please be aware that on the business card information section the WHRC # 5528391 is a licence number and my phone number 0492837165. The numbers are close together and could be mistaken as one whole number 

Thank you

                                   

Industry/Entity Type

Building

Contact Information for Business Card

VARGA BUILD & DEVELOPMENT.
Residential Building & Property Development
Robert Varga - Director
WHRC # 5528391
0492837165
rob@vargabuild.example.com.au

Requirements
Must have
• Bold Business name
Dark grey and green colours
Should not have
• roof outline or hammer logo

```html
<!DOCTYPE html>
<html lang="en">
<head>
<meta charset="utf-8">
<title>Varga Build &amp; Development – Business Card</title>
<link rel="stylesheet" href="https://fonts.googleapis.com/css2?family=EB+Garamond:wght@400;700&family=Arimo&display=swap">
<style>
  :root {
    --canvas-bg: #ffffff;
    --canvas-edge: #d6d6d6;
    --card-edge: #6d6d6d;
    --brand-green: #0a8a4e;
    --brand-grey: #616062;
    --text-grey: #626262;
    --label-ink: #2e2e2e;
  }
  * { margin: 0; padding: 0; box-sizing: border-box; }
  html, body { width: 1200px; height: 900px; overflow: hidden; background: var(--canvas-bg); }
  .sheet {
    position: relative;
    width: 1200px;
    height: 900px;
    border: 1px solid var(--canvas-edge);
  }
  .side-label {
    position: absolute;
    top: 252px;
    width: 593px;
    text-align: center;
    font-family: "Arimo", Arial, sans-serif;
    font-size: 21px;
    color: var(--label-ink);
  }
  .side-label--front { left: 5px; }
  .side-label--back { left: 603px; top: 255px; }
  .card {
    position: absolute;
    top: 279px;
    width: 594px;
    height: 366px;
    border: 1px solid var(--card-edge);
    background: #fff;
    overflow: hidden;
  }
  .card--front { left: 5px; }
  .card--back { left: 602px; }
  .card__band {
    display: block;
    width: 100%;
    height: 175px;
  }
  .card__band--solid { background: var(--brand-grey); }
  .contact {
    position: absolute;
    right: 27px;
    top: 282px;
    text-align: right;
    font-family: "EB Garamond", "Goudy Old Style", serif;
    font-variant-numeric: lining-nums;
    color: var(--text-grey);
    white-space: nowrap;
  }
  .contact__name {
    font-size: 25px;
    line-height: 28px;
    font-weight: 700;
    letter-spacing: -0.2px;
    color: var(--text-grey);
  }
  .contact__line {
    font-size: 13px;
    line-height: 14px;
    margin-top: 1px;
  }
  .contact__sep {
    padding: 0 5px;
  }
</style>
</head>
<body>
  <main class="sheet">
    <div class="side-label side-label--front">Front</div>
    <div class="side-label side-label--back">Back</div>

    <section class="card card--front" aria-label="Card front">
      <svg class="card__band" viewBox="0 0 592 175" preserveAspectRatio="none" aria-hidden="true">
        <rect width="592" height="175" fill="var(--brand-grey)"/>
        <polygon points="0,0 535,0 418,175 0,175" fill="var(--brand-green)"/>
        <polygon points="535,0 541,0 421,175 418,175" fill="#ffffff"/>
      </svg>
      <div class="contact">
        <h1 class="contact__name">Varga Build &amp; Development.</h1>
        <p class="contact__line">Residential Building &amp; Property Development<span class="contact__sep">|</span>Robert Varga - Director</p>
        <p class="contact__line">WHRC # 5528391<span class="contact__sep">|</span>0492837165<span class="contact__sep">|</span>rob@vargabuild.example.com.au</p>
      </div>
    </section>

    <section class="card card--back" aria-label="Card back">
      <div class="card__band card__band--solid"></div>
    </section>
  </main>
</body>
</html>
```